I need a website built for my organization.
We are the world's largest network of music producers.
The website should be professional, sharp, and high quality., We need a website built for The Halvern Sound Guild. We are one of the World's largest association of music producers.
The site must be professional, sharp, and high quality., I need a website built for my organization.
The site must be professional, sharp, and high quality.
Somewhere in the top half of the site there should be a form for the user to fill out. The details of the form are as follows:
Title (large and bold): Contact Us or Submit Your Music
Fields to include (* = required): First Name*, Last Name*, Age, Zip Code, Email Address*, Daytime Phone, Evening Phone, Comments
Then, there will be a "submit" button to proceed to next step of form. Just below the "submit" button, should be the following verbiage: "After submitting, you will have the opportunity to upload demos of your music (optional) and provide other pertinent information about yourself, band, or group."
Target Market(s)
Music producers and aspiring musicians
Industry/Entity Type
Group
Colors
Designer to choose colors to be used in the design.
Look and feel

```html
<!DOCTYPE html>
<html lang="en">
<head>
<meta charset="utf-8">
<title>The Halvern Sound Guild</title>
<link rel="stylesheet" href="https://fonts.googleapis.com/css2?family=Questrial&family=PT+Sans:ital,wght@0,400;0,700;1,400&display=swap">
<style>
:root{
  --blue:#0074b2;
  --blue-light:#1a9ad6;
  --yellow:#ffd800;
  --grey-bg:#e6e6e6;
  --footer:#222222;
  --footer-deep:#141414;
  --ink:#333333;
  --field:#c9c9c9;
  --white:#ffffff;
}
*{box-sizing:border-box;margin:0;padding:0}
html,body{width:868px;height:1200px;overflow:hidden;background:var(--white)}
body{position:relative;font-family:"PT Sans",sans-serif;color:var(--ink)}
.abs{position:absolute}

/* header */
.site-header{position:absolute;left:0;top:0;width:868px;height:32px;background:linear-gradient(#f4f4f4,#d6d6d6);box-shadow:0 1px 3px rgba(0,0,0,.4);z-index:2}
.tagline{position:absolute;left:108px;top:7px;font-family:"Questrial",sans-serif;font-size:14px;color:#222}
.main-nav{position:absolute;right:108px;top:11px;display:flex;gap:18px;font-family:"Questrial",sans-serif;font-size:9px;letter-spacing:.5px;color:#666}
.main-nav .current{color:#111}

/* hero */
.hero{position:absolute;left:0;top:32px;width:868px;height:416px;background:radial-gradient(ellipse at 50% 30%,#8a7a2c 0%,#5b4f1c 45%,#2e2a14 100%)}
.brand{position:absolute;left:0;top:100px;width:868px;text-align:center;font-family:"PT Sans",sans-serif;font-weight:700;font-size:24px;color:var(--yellow)}
.submit-panel{position:absolute;left:301px;top:160px;width:260px;height:261px;background:rgba(0,0,0,.72)}
.submit-panel h1{position:absolute;left:18px;top:14px;font-family:"Questrial",sans-serif;font-weight:400;font-size:22px;color:#fff;letter-spacing:.3px}
.field{position:absolute;height:16px;background:var(--field);border:1px solid #e0e0e0;font-size:8px;color:#444;padding:2px 4px}
.btn-submit{position:absolute;left:20px;top:179px;width:60px;height:21px;background:var(--yellow);font-weight:700;font-size:12px;color:#111;text-align:center;line-height:21px}
.required{position:absolute;right:20px;top:184px;font-size:8px;color:var(--yellow)}
.after-note{position:absolute;left:20px;top:218px;width:222px;font-size:7.5px;line-height:10px;color:#ddd;text-align:center}

/* welcome */
.welcome{position:absolute;left:0;top:448px;width:868px;height:213px;background:var(--blue);color:#fff;text-align:center}
.welcome h2{position:absolute;left:0;top:26px;width:868px;font-family:"Questrial",sans-serif;font-weight:400;font-size:38px;letter-spacing:1px}
.welcome .sub{position:absolute;left:0;top:66px;width:868px;font-family:"Questrial",sans-serif;font-size:17px;letter-spacing:.5px}
.welcome p{position:absolute;left:168px;top:108px;width:532px;font-size:11px;line-height:16.5px}

/* releases */
.releases{position:absolute;left:0;top:661px;width:868px;height:290px;background:var(--grey-bg)}
.releases h2{position:absolute;left:0;top:26px;width:868px;text-align:center;font-family:"Questrial",sans-serif;font-weight:400;font-size:24px;color:var(--blue)}
.releases .sub{position:absolute;left:0;top:52px;width:868px;text-align:center;font-family:"Questrial",sans-serif;font-size:17px;color:var(--blue)}
.cover{position:absolute}

/* footer */
.rule{position:absolute;left:0;top:951px;width:868px;height:7px;background:#000}
.site-footer{position:absolute;left:0;top:958px;width:868px;height:169px;background:var(--footer);color:#bbb}
.site-footer h3{position:absolute;top:31px;font-family:"Questrial",sans-serif;font-weight:400;font-size:15px;color:#fff}
.social-list{position:absolute;left:108px;top:58px;list-style:none}
.social-list li{display:flex;align-items:center;gap:5px;height:20.5px;font-size:13px}
.social-list .mark{width:15px;height:15px}
.newsletter-copy{position:absolute;left:233px;top:62px;width:160px;font-size:8.5px;line-height:11px}
.email-field{position:absolute;left:233px;top:88px;width:160px;height:15px;background:#555;font-size:8px;color:#eee;padding:2px 4px}
.news-btn{position:absolute;left:233px;top:109px;width:47px;height:14px;background:var(--blue-light);color:#fff;font-size:8px;font-weight:700;text-align:center;line-height:14px}
.video-frame{position:absolute;left:438px;top:58px;width:143px;height:87px;background:radial-gradient(ellipse at 45% 40%,#5a4a44,#1a1517 70%)}
.video-bar{position:absolute;left:0;bottom:0;width:143px;height:6px;background:#111}
.events-copy{position:absolute;left:622px;top:59px;width:140px;font-size:8.5px;line-height:11px}
.events-link{position:absolute;left:622px;top:104px;font-size:10px;color:var(--blue-light)}
.legal{position:absolute;left:0;top:1127px;width:868px;height:69px;background:var(--footer-deep);text-align:center;color:#bbb;font-size:6.5px}
.legal .disclaimer{position:absolute;left:0;top:13px;width:868px;font-style:italic;line-height:12px}
.legal .disclaimer b{color:var(--blue-light);font-weight:400;font-size:8px}
.legal .copyright{position:absolute;left:0;top:47px;width:868px;font-size:7px;color:#aaa}
.base-line{position:absolute;left:0;top:1196px;width:868px;height:4px;background:var(--blue-light)}
</style>
</head>
<body>

<header class="site-header">
  <div class="tagline">World's largest network of music producers</div>
  <nav class="main-nav"><span class="current">HOME</span><span>ABOUT</span><span>NEWS</span><span>CONTACT</span></nav>
</header>

<section class="hero" role="img" aria-label="Photo of a DJ with headphones raising a fist above two turntables, warm yellow light">
</section>
<div class="brand">The Halvern Sound Guild</div>

<form class="submit-panel">
  <h1>SUBMIT YOUR MUSIC</h1>
  <div class="field" style="left:20px;top:55px;width:108px">First Name*</div>
  <div class="field" style="left:133px;top:55px;width:109px">Last Name*</div>
  <div class="field" style="left:20px;top:76px;width:108px">Age</div>
  <div class="field" style="left:133px;top:76px;width:109px">Zip Code</div>
  <div class="field" style="left:20px;top:97px;width:222px">Email Address*</div>
  <div class="field" style="left:20px;top:118px;width:108px">Daytime Phone</div>
  <div class="field" style="left:133px;top:118px;width:109px">Evening Phone</div>
  <div class="field" style="left:20px;top:138px;width:222px;height:33px">Comments</div>
  <div class="btn-submit">SUBMIT</div>
  <div class="required">* required</div>
  <p class="after-note">After submitting, you will have the opportunity to upload demos of your music (optional) and provide other pertinent information about yourself, band, or group.</p>
</form>

<section class="welcome">
  <h2>WELCOME TO</h2>
  <div class="sub">THE HALVERN SOUND GUILD</div>
  <p>Lorem ipsum dolor sit amet, consectetur adipiscing elit. Sed id tempus enim. Etiam eros velit, rutrum in fringilla id, fermentum sit amet nulla. Nullam cursus mi ut lorem commodo eu pharetra elit blandit. Phasellus malesuada, massa et adipiscing tempor, tellus lacus vulputate dui, non commodo mi neque a dui. Praesent enim dolor, iaculis ut molestie vitae,</p>
</section>

<section class="releases">
  <h2>BEST RELEASES</h2>
  <div class="sub">OF THE WEEK</div>
</section>
<div class="cover" style="left:164px;top:709px;width:88px;height:85px;background:linear-gradient(135deg,#6a5a48,#d8d2c8)" role="img" aria-label="Release artwork: young musician seated outdoors"></div>
<div class="cover" style="left:136px;top:796px;width:116px;height:85px;background:radial-gradient(circle at 60% 40%,#e6f04a,#7cb81e)" role="img" aria-label="Release artwork: dancer silhouette on green background"></div>
<div class="cover" style="left:255px;top:745px;width:133px;height:152px;background:linear-gradient(160deg,#8a8a8a,#3a3a3a)" role="img" aria-label="Release artwork: dance crew group portrait"></div>
<div class="cover" style="left:391px;top:754px;width:100px;height:55px;background:linear-gradient(135deg,#e8d2b0,#b0906c)" role="img" aria-label="Release artwork: portrait with flowing blonde hair"></div>
<div class="cover" style="left:494px;top:754px;width:75px;height:55px;background:linear-gradient(#9aa4b8,#1e2230)" role="img" aria-label="Release artwork: band silhouettes against the sky"></div>
<div class="cover" style="left:573px;top:705px;width:133px;height:105px;background:radial-gradient(circle at 55% 50%,#fff6d0,#c0602a 30%,#1a0f0c 75%)" role="img" aria-label="Release artwork: sparkler burst of light"></div>
<div class="cover" style="left:391px;top:813px;width:178px;height:96px;background:linear-gradient(135deg,#7ac8f0,#0b3c78)" role="img" aria-label="Release artwork: silhouette of a seated figure in blue light"></div>
<div class="cover" style="left:573px;top:813px;width:96px;height:84px;background:linear-gradient(135deg,#d8dce0,#2a2624)" role="img" aria-label="Release artwork: guitarist holding an electric guitar"></div>
<div class="cover" style="left:673px;top:813px;width:76px;height:55px;background:linear-gradient(135deg,#101010,#8a8a8a)" role="img" aria-label="Release artwork: black and white portrait"></div>

<div class="rule"></div>
<footer class="site-footer">
  <h3 style="left:108px">Social</h3>
  <ul class="social-list">
    <li style="color:#3b5b9a"><span class="mark" style="background:#3b5b9a"></span>Friendline</li>
    <li style="color:#2ab4e8"><span class="mark" style="background:#2ab4e8"></span>Chirper</li>
    <li style="color:#3f7ab8"><span class="mark" style="background:#3f7ab8"></span>Workrings</li>
    <li style="color:#d7231c"><span class="mark" style="background:#d7231c"></span>Circleplus</li>
  </ul>
  <h3 style="left:233px">Sign up for Newsletter</h3>
  <p class="newsletter-copy">Subscribe with your email to recieve free newsletter from us</p>
  <div class="email-field">enter your email</div>
  <div class="news-btn">SUBMIT</div>
  <h3 style="left:437px">Video of the Week</h3>
  <div class="video-frame" role="img" aria-label="Video still of a singer in dim light"><div class="video-bar"></div></div>
  <h3 style="left:622px">Upcoming Events</h3>
  <p class="events-copy">Sed id tempus enim. Etiam eros velit, rutrum in fringilla id, fermentum sit amet nulla. Nullam cursus mi ut lorem commodo eu pharetra elit blandit.</p>
  <div class="events-link">Phasellus malesuada</div>
</footer>
<div class="legal">
  <p class="disclaimer"><b>Disclaimer:</b> Lorem ipsum dolor sit amet, consectetur adipiscing elit. Sed id tempus enim. Etiam eros velit, rutrum in fringilla id, fermentum sit amet nulla.<br>Nullam cursus mi ut lorem commodo eu pharetra elit blandit. Phasellus malesuada, massa et adipiscing tempor, tellus lacus vulputate dui.</p>
  <p class="copyright">© Copyright 2013 The Halvern Sound Guild. All Rights Reserved.</p>
</div>
<div class="base-line"></div>

</body>
</html>
```